Rosalind Vetteray Gymnastics Center Business Card

Develop a business card with my RV logo provided. A classy and unique design using the colors black, white, purple and maybe a splash of gold. Add Address (219 W. Lantern Ridge Road Medina, Ohio 44871), email (RosalindVetterayGymnasticsCtr@brellomail.com, website (www.RosalindVetterayGymnasticsCenter.example), phone number (216-555-0148) on the card. Social media if there's room also. t: @VetterayGym, i: @VetterayGym, f: @RosalindVetterayGymnasticsCenter

Target Market(s)

Families, children, gymnastics community and beyond

Industry/Entity Type

Business

Contact Information for Business Card

Add name (Rosalind Vetteray) who is the owner. Add logo, add address details, classy font, uniqueness important, rounded edges on business card. Horizontal business card needed.

Font styles to use
Serif
Sans Serif

Colors
6b449b
ffffff

Requirements
Must have
• Must have logo, owner name and owner on card, must have colors purple, white, black where needed in print, and a splash of gold if appropriate. Keep card classy and clean. Must have address of location, phone number, website of business, email and social media.
Nice to have
• I am open here, but I'd appreciate uniqueness. Must be a lasting image for branding...
Should not have
• No kid-like looks...

```html
<!DOCTYPE html>
<html lang="en">
<head>
<meta charset="utf-8">
<title>Rosalind Vetteray Gymnastics Center – Business Card</title>
<link href="https://fonts.googleapis.com/css2?family=Cinzel:wght@700&family=Lato:wght@400&family=Cormorant+Garamond:wght@500&display=swap" rel="stylesheet">
<style>
  :root {
    --stage: #535353;
    --purple: #662d91;
    --purple-soft: #7a44a8;
    --white: #ffffff;
    --rule: rgba(255,255,255,0.55);
    --black: #000000;
  }
  * { margin: 0; padding: 0; box-sizing: border-box; }
  html, body { width: 1200px; height: 900px; overflow: hidden; }
  body { background: var(--stage); position: relative; font-family: 'Lato', sans-serif; }

  .card {
    position: absolute; top: 170px; width: 346px; height: 560px;
    box-shadow: 3px 4px 8px rgba(0,0,0,0.45);
  }
  .card--info { left: 260px; background: var(--purple); color: var(--white); text-align: center; }
  .card--brand { left: 631px; background: var(--black); overflow: hidden; }

  .owner-name {
    position: absolute; top: 88px; width: 100%;
    font-family: 'Cinzel', serif; font-weight: 700; font-size: 21px; letter-spacing: 0.5px;
  }
  .owner-title { position: absolute; top: 119px; width: 100%; font-size: 15px; }

  .divider { position: absolute; left: 0; width: 100%; height: 28px; }
  .divider--location { top: 159px; }
  .divider--contact { top: 264px; }
  .divider--social { top: 383px; }

  .text-block { position: absolute; width: 100%; }
  .address { top: 197px; font-size: 16px; line-height: 20px; }
  .contact { top: 300px; font-size: 13.5px; line-height: 17px; }
  .social { top: 418px; font-size: 16px; line-height: 20px; }

  .brand-backdrop {
    position: absolute; inset: 0;
    background: radial-gradient(ellipse at 50% 40%, #1a1a1a 0%, #0d0d0d 55%, #000 100%);
  }
  .brand-dot {
    position: absolute; top: 188px; left: 116px; width: 114px; height: 114px;
    border-radius: 50%; background: var(--purple);
  }
  .brand-name {
    position: absolute; top: 303px; width: 100%; text-align: center;
    font-family: 'Cinzel', serif; font-weight: 700; font-size: 19.5px; line-height: 23px;
    color: var(--white); letter-spacing: 0.3px;
  }
  .brand-rule { position: absolute; top: 352px; left: 36px; width: 276px; height: 1px; background: var(--purple-soft); }
  .brand-tagline {
    position: absolute; top: 354px; width: 100%; text-align: center;
    font-family: 'Cormorant Garamond', serif; font-weight: 500; font-size: 18px;
    color: var(--purple-soft);
  }
</style>
</head>
<body>

<section class="card card--info">
  <h1 class="owner-name">Rosalind Vetteray</h1>
  <p class="owner-title">Owner</p>

  <svg class="divider divider--location" viewBox="0 0 346 28">
    <line x1="74" y1="14" x2="159" y2="14" stroke="var(--rule)"/>
    <line x1="187" y1="14" x2="272" y2="14" stroke="var(--rule)"/>
    <circle cx="173" cy="14" r="13" fill="var(--white)"/>
    <path d="M173 6.5a5 5 0 0 0-5 5c0 4 5 9.5 5 9.5s5-5.5 5-9.5a5 5 0 0 0-5-5z" fill="var(--purple)"/>
    <circle cx="173" cy="11.5" r="1.9" fill="var(--white)"/>
  </svg>
  <p class="text-block address">219 W. Lantern Ridge Road<br>Medina, Ohio 44871</p>

  <svg class="divider divider--contact" viewBox="0 0 346 28">
    <line x1="71" y1="14" x2="128" y2="14" stroke="var(--rule)"/>
    <line x1="218" y1="14" x2="273" y2="14" stroke="var(--rule)"/>
    <circle cx="142" cy="14" r="13" fill="var(--white)"/>
    <path d="M136 10.5c2-2 10-2 12 0v2h-3v-1.5h-6v1.5h-3z M138 13h8l1.5 5h-11z" fill="var(--purple)"/>
    <circle cx="172" cy="14" r="13" fill="var(--white)"/>
    <rect x="165" y="9.5" width="14" height="9" fill="var(--purple)"/>
    <path d="M165 9.5l7 5.5 7-5.5" fill="none" stroke="var(--white)" stroke-width="1.2"/>
    <circle cx="202" cy="14" r="13" fill="var(--white)"/>
    <circle cx="202" cy="14" r="6.5" fill="none" stroke="var(--purple)" stroke-width="1.6"/>
    <path d="M195.5 14h13M202 7.5c-3 3.5-3 9.5 0 13M202 7.5c3 3.5 3 9.5 0 13" fill="none" stroke="var(--purple)" stroke-width="1.2"/>
  </svg>
  <p class="text-block contact">216-555-0148<br>RosalindVetterayGymnasticsCtr@brellomail.com<br>www.RosalindVetterayGymnasticsCenter.example</p>

  <svg class="divider divider--social" viewBox="0 0 346 28">
    <line x1="71" y1="14" x2="128" y2="14" stroke="var(--rule)"/>
    <line x1="218" y1="14" x2="273" y2="14" stroke="var(--rule)"/>
    <!-- chat bubble -->
    <circle cx="142" cy="14" r="13" fill="var(--white)"/>
    <path d="M135.5 8.5h13v8.5h-7l-3.5 3v-3h-2.5z" fill="var(--purple)"/>
    <!-- share nodes -->
    <circle cx="172" cy="14" r="13" fill="var(--white)"/>
    <path d="M167.5 14l8-4.5M167.5 14l8 4.5" stroke="var(--purple)" stroke-width="1.5"/>
    <circle cx="167.5" cy="14" r="2.3" fill="var(--purple)"/>
    <circle cx="176" cy="9.3" r="2.3" fill="var(--purple)"/>
    <circle cx="176" cy="18.7" r="2.3" fill="var(--purple)"/>
    <!-- link -->
    <circle cx="202" cy="14" r="13" fill="var(--white)"/>
    <rect x="195" y="11" width="8" height="6" rx="3" fill="none" stroke="var(--purple)" stroke-width="1.6"/>
    <rect x="201" y="11" width="8" height="6" rx="3" fill="none" stroke="var(--purple)" stroke-width="1.6"/>
  </svg>
  <p class="text-block social">@VetterayGym<br>@VetterayGym<br>@RosalindVetterayGymnasticsCenter</p>
</section>

<section class="card card--brand">
  <div class="brand-backdrop" role="img" aria-label="Dark background with a faint repeating brand pattern"></div>
  <div class="brand-dot"></div>
  <h2 class="brand-name">Rosalind Vetteray<br>Gymnastics Center</h2>
  <div class="brand-rule"></div>
  <p class="brand-tagline">Gymnastics, Camps, Yoga &amp; More</p>
</section>

</body>
</html>
```